Young Adult Retreat Needs Event Promo Graphics

I need graphics designed for our summer young adult (18 years old - 30 years old) camp-style retreat. This event will take place at a campground in the black hills of South Dakota. Primary graphic design is for a 11x17 poster but will also need the images resized for:

-social media: square; can include only main titles or main titles and speaker
-16x9 title slide that includes: titles, full background images, organization logo, and website. No camp speaker or dates, no additional info.
- a postcard size (4.25in x 6in) with all content on it

All graphics need to be print quality (300 dpi or higher)

11x17 main poster design should include the following:
-Main Title: PR Brightway (or logo) presents . . . Prairie Ridge Young Adult Retreat
-Dates: June 3-5th, 2022
-Register at PRBrightway.com
-Cedar Fork Lodge Center, Deadwood, SD
-Speaker: Marla Tovin (photo attached)
-Include PR Brightway logo
-Event Graphic should be attractive to 18-30 year olds but SHOULD NOT include references to alcohol, sexuality, drugs, or profanity.

My graphic design experience is limited. I will need help receiving the files I need in the various sizes. Thank you.

```html
<!DOCTYPE html>
<html lang="en">
<head>
<meta charset="utf-8">
<title>Prairie Ridge Young Adult Retreat</title>
<link rel="stylesheet" href="https://fonts.googleapis.com/css2?family=Amatic+SC:wght@700&family=Poiret+One&family=PT+Sans+Narrow:wght@400;700&display=swap">
<style>
  :root {
    --ink: #1c1a22;
    --sky-top: #9f9bd6;
    --sky-mid: #f3e8f6;
    --sky-pink: #f2b8d8;
    --sky-low: #c7a4d6;
    --brand: #2fa8e6;
    --title-plum: #7a1470;
    --title-magenta: #e0176a;
    --title-pink: #ff1a66;
    --title-orange: #ff6a45;
    --forest-red: #c8195e;
    --forest-blue: #9fc9f0;
  }
  * { margin: 0; padding: 0; box-sizing: border-box; }
  html, body { width: 771px; height: 1200px; overflow: hidden; background: #fff; }
  .poster {
    position: relative;
    width: 771px;
    height: 1200px;
    overflow: hidden;
    color: var(--ink);
    font-family: "PT Sans Narrow", sans-serif;
  }
  .sky {
    position: absolute; inset: 0;
    background:
      radial-gradient(circle at 150px 300px, rgba(255,255,255,0.95) 0, rgba(255,255,255,0.5) 60px, rgba(255,255,255,0) 170px),
      radial-gradient(ellipse 330px 360px at 390px 520px, rgba(255,255,255,0.85), rgba(255,255,255,0) 100%),
      linear-gradient(180deg, var(--sky-top) 0%, #c9bfe6 22%, var(--sky-mid) 42%, var(--sky-pink) 62%, var(--sky-low) 80%, #f0c8e2 90%);
  }
  .forest {
    position: absolute; left: 0; right: 0; bottom: 0; height: 180px;
    background:
      linear-gradient(180deg, rgba(240,200,226,0) 0%, rgba(159,201,240,0.7) 30%, rgba(200,25,94,0.55) 75%, var(--forest-red) 100%),
      linear-gradient(90deg, var(--forest-red) 0%, var(--forest-blue) 30%, var(--forest-blue) 70%, var(--forest-red) 100%);
  }
  .brand {
    position: absolute; left: 26px; top: 42px;
    display: flex; align-items: center; gap: 12px;
  }
  .brand-name {
    font-weight: 700; font-size: 30px; color: var(--brand); line-height: 1;
  }
  .brand-presents {
    font-size: 24px; letter-spacing: 0.5px; line-height: 1;
  }
  .speaker {
    position: absolute; left: 360px; top: 116px; width: 160px;
    text-align: center; line-height: 1.2;
  }
  .speaker-label { font-size: 21px; }
  .speaker-name { font-size: 23px; font-weight: 700; text-transform: uppercase; }
  .speaker-photo {
    position: absolute; left: 525px; top: 20px; width: 230px; height: 230px;
    border-radius: 50%;
    background: radial-gradient(circle at 50% 45%, #c99a7e 0, #8a5a44 45%, #e8ddd8 100%);
    box-shadow: 0 0 0 2px rgba(255,255,255,0.6);
  }
  .title { position: absolute; left: 0; width: 771px; text-align: center; }
  .title-place {
    top: 300px; font-family: "Poiret One", sans-serif; font-size: 58px; letter-spacing: 1px; padding-left: 6px;
  }
  .title-main, .title-retreat {
    font-family: "Amatic SC", sans-serif; font-weight: 700; line-height: 1;
    -webkit-background-clip: text; background-clip: text; color: transparent;
  }
  .title-main {
    top: 400px; font-size: 136px; letter-spacing: 2px;
    background-image: linear-gradient(180deg, var(--title-plum) 20%, var(--title-magenta) 85%);
  }
  .title-retreat {
    top: 515px; font-size: 212px; letter-spacing: 2px;
    background-image: linear-gradient(180deg, var(--title-pink) 25%, var(--title-orange) 85%);
  }
  .dates {
    top: 745px; font-family: "Poiret One", sans-serif; font-size: 38px;
  }
  .venue {
    top: 915px; font-size: 27px; font-weight: 700; line-height: 1.45;
  }
  .register {
    top: 993px; font-size: 22px;
  }
</style>
</head>
<body>
  <main class="poster">
    <div class="sky" role="img" aria-label="Soft lavender and pink sky with a bright starburst of light"></div>
    <div class="forest" role="img" aria-label="Tinted view of forested hills along the bottom edge"></div>

    <header class="brand">
      <span class="brand-name">PR Brightway</span>
      <span class="brand-presents">PRESENTS</span>
    </header>

    <div class="speaker">
      <p class="speaker-label">Speaker:</p>
      <p class="speaker-name">Marla Tovin</p>
    </div>
    <div class="speaker-photo" role="img" aria-label="Portrait photo of speaker Marla Tovin"></div>

    <h1>
      <span class="title title-place">Prairie Ridge</span>
      <span class="title title-main">YOUNG ADULT</span>
      <span class="title title-retreat">RETREAT</span>
    </h1>

    <p class="title dates">June 3-5th, 2022</p>
    <p class="title venue">Cedar Fork Lodge Center,<br>Deadwood, SD</p>
    <p class="title register">Register at PRBrightway.com</p>
  </main>
</body>
</html>
```